Plakat-Design für Immobilienvertrieb
Zielgruppe
Wir sind ein Nürnberger Immobilienvertrieb mit Schwerpunkt Verkauf von Häusern und Eigentumswohnungen. Wir bauen nach und nach unsere Multi-Channel-Präsenz auf, wozu auch ein Plakat ein einem Nürnberger Parkhaus (Innenstadtlage und gegenüber vom größten Kino Nürnbergs) zählt. Das Plakat befindet sich im Kassenbereich (Foto anbei) und soll daher möglichst auffällig sein.
Zielgruppe: Eigentümer von Immobilien im Alter 40+
Ziel: Aufmerksamkeit schaffen
Stil: Modern und gerne ungewöhnlicher. In jedem Fall muss man mit dem Auge hängen bleiben.
Aufgabenstellung
Format: DIN A0, PSD und druckfähiges PDF
Logo, Telefonnummer und www.hauskompass24.de müssen immer drauf sein
Wir könnten uns für das Plakat folgende Ansätze vorstellen - andere Vorschläge sind aber gerne gesehen. Uns ist es wichtig, dass wir ein Plakat fern ab vom Schema-F erhalten. Wir suchen nach einer witzigen und ansprechenden Idee.
1. Die klassische Variante: Unser Claim 'Aus Liebe zu Nürnberg entsteht Leidenschaft für den Immobilienvertrieb.' als Aufhänger für das Plakat (Nürnberg-Bilder anbei). Inhaltlich geht es dann weiter mit unseren Leistungen: Verkauf, Vermietung, Bauträgervertrieb
2. 'Keine Lust mehr auf Rasenmähen?' als Aufhänger - mit der Message wollen wir vor allem die ältere Zielgruppe ansprechen, die ihr Haus verkaufen und in eine komfortablere Wohnung umziehen will. Die Botschaft soll dann weiter gehen mit 'Wir unterstützen Sie beim Verkauf Ihrer Immobilie. Starten Sie jetzt mit einer kostenfreien Immobilienbewertung.' Hier müsste ein witziges Bild eingebunden werden, das zum Beispiel einen ungebändigten Garten o.ä. zeigt.
3. Filmplakat in Anlehnung an das benachbarte Kino: Ein Filmklassiker (oder aktueller Film) soll umgemünzt werden auf das Immobilienthema - Kernbotschaft ist immer, dass wir uns um den Verkauf der Immobilie kümmern, stressfrei für den Eigentümer.
4. Mega-Brumm-Zitat - basierend auf dem dritten Filmansatz könnten wir uns auch ein Illustration vorstellen (Bild anbei), die Mega Brumm in Nürnberg zeigt (z.B. auf der Ortwinskirche) und mit dem Aufhänger 'Damit Ihr Immobilienverkauf nicht zum Drama wird.' Außerdem muss dann weiter auf das Plakat 'Wir unterstützen Sie beim Verkauf Ihrer Immobilie. Starten Sie jetzt mit einer kostenfreien Immobilienbewertung.'
Sollten Stockbilder verwendet werden, dann bitte nur von bildquello.com - danke!

```html
<!DOCTYPE html>
<html lang="de">
<head>
<meta charset="utf-8">
<title>Plakat Immobilienvertrieb</title>
<link rel="stylesheet" href="https://fonts.googleapis.com/css2?family=Lilita+One&family=Montserrat:ital,wght@0,700;1,800;1,900&display=swap">
<style>
  :root {
    --blue: #1a98d5;
    --navy: #1a1f33;
    --white: #ffffff;
    --stripe-grey: #e8e8ea;
  }
  html, body {
    margin: 0;
    padding: 0;
    overflow: hidden;
    background: var(--white);
  }
  .poster {
    position: relative;
    width: 846px;
    height: 1200px;
    overflow: hidden;
    background: var(--white);
  }
  .poster-art {
    position: absolute;
    inset: 0;
    display: block;
  }
  .headline {
    position: absolute;
    top: 36px;
    left: 0;
    width: 846px;
    margin: 0;
    text-align: center;
    font-family: "Montserrat", sans-serif;
    font-style: italic;
    font-weight: 900;
    font-size: 41px;
    line-height: 55px;
    letter-spacing: -1px;
    color: var(--white);
    text-shadow: 3px 3px 0 var(--navy);
  }
  .label {
    font-family: "Lilita One", sans-serif;
    text-transform: uppercase;
  }
  .contact {
    font-family: "Montserrat", sans-serif;
    font-style: italic;
    font-weight: 800;
    font-size: 25px;
    fill: var(--white);
  }
  .brand-name {
    position: absolute;
    top: 1108px;
    left: 0;
    width: 846px;
    text-align: center;
    font-family: "Montserrat", sans-serif;
    font-weight: 700;
    font-size: 38px;
    letter-spacing: 1px;
    color: var(--navy);
  }
</style>
</head>
<body>
<div class="poster">
  <svg class="poster-art" width="846" height="1200" viewBox="0 0 846 1200" xmlns="http://www.w3.org/2000/svg">
    <defs>
      <linearGradient id="city-tones" x1="0" y1="0" x2="1" y2="1">
        <stop offset="0" stop-color="#8f8a78"/>
        <stop offset="0.35" stop-color="#5e7b45"/>
        <stop offset="0.6" stop-color="#a46a4c"/>
        <stop offset="1" stop-color="#c9c3b8"/>
      </linearGradient>
    </defs>

    <!-- top band -->
    <rect class="band-top" x="0" y="0" width="846" height="168" fill="var(--blue)"/>

    <!-- city photo area -->
    <rect x="0" y="167" width="846" height="500" fill="url(#city-tones)" role="img" aria-label="Luftaufnahme der Nürnberger Altstadt mit Kirchen und Dächern"/>

    <!-- bottom blue band -->
    <rect x="0" y="880" width="846" height="172" fill="var(--blue)"/>

    <!-- dark diagonal field -->
    <polygon points="0,644 846,487 846,897 0,940" fill="var(--navy)"/>

    <!-- accent stripes -->
    <g stroke-width="5">
      <line x1="0" y1="620" x2="108" y2="600" stroke="var(--blue)"/>
      <line x1="420" y1="503" x2="596" y2="470" stroke="var(--stripe-grey)"/>
      <line x1="699" y1="511" x2="846" y2="487" stroke="var(--navy)"/>
      <line x1="676" y1="595" x2="846" y2="566" stroke="var(--blue)"/>
      <line x1="56" y1="702" x2="233" y2="666" stroke="var(--blue)"/>
      <line x1="117" y1="715" x2="160" y2="706" stroke="var(--stripe-grey)"/>
      <line x1="558" y1="675" x2="735" y2="641" stroke="var(--stripe-grey)"/>
      <line x1="662" y1="680" x2="840" y2="646" stroke="var(--stripe-grey)"/>
      <line x1="0" y1="800" x2="150" y2="770" stroke="var(--blue)"/>
      <line x1="563" y1="804" x2="740" y2="769" stroke="var(--blue)"/>
      <line x1="617" y1="816" x2="795" y2="784" stroke="var(--stripe-grey)"/>
    </g>

    <!-- service boxes -->
    <polygon points="156,483 390,445 390,524 156,567" fill="var(--blue)"/>
    <polygon points="156,576 712,484 712,565 156,664" fill="var(--blue)"/>
    <polygon points="156,681 544,628 544,686 156,754" fill="var(--white)"/>
    <polygon points="318,746 707,683 707,741 318,806" fill="var(--white)"/>
    <polygon points="144,859 533,795 533,851 144,921" fill="var(--white)"/>

    <g class="label">
      <g transform="translate(184,535) rotate(-9.5)">
        <text x="2" y="2" font-size="40" fill="var(--navy)">Für den</text>
        <text x="0" y="0" font-size="40" fill="var(--white)">Für den</text>
      </g>
      <g transform="translate(182,633) rotate(-9.5)">
        <text x="2" y="2" font-size="42" fill="var(--navy)" textLength="506" lengthAdjust="spacingAndGlyphs">Immobilienvertrieb</text>
        <text x="0" y="0" font-size="42" fill="var(--white)" textLength="506" lengthAdjust="spacingAndGlyphs">Immobilienvertrieb</text>
      </g>
      <g transform="translate(289,712) rotate(-9.5)">
        <text x="2" y="2" font-size="28" fill="var(--blue)">Verkauf</text>
        <text x="0" y="0" font-size="28" fill="var(--navy)">Verkauf</text>
      </g>
      <g transform="translate(419,772) rotate(-9.5)">
        <text x="2" y="2" font-size="28" fill="var(--blue)">Vermietung</text>
        <text x="0" y="0" font-size="28" fill="var(--navy)">Vermietung</text>
      </g>
      <g transform="translate(182,893) rotate(-9.5)">
        <text x="2" y="2" font-size="28" fill="var(--blue)" textLength="330" lengthAdjust="spacingAndGlyphs">Bauträgervertrieb</text>
        <text x="0" y="0" font-size="28" fill="var(--navy)" textLength="330" lengthAdjust="spacingAndGlyphs">Bauträgervertrieb</text>
      </g>
    </g>

    <!-- contact row -->
    <g class="contact-phone">
      <circle cx="87" cy="997" r="25" fill="var(--white)"/>
      <path d="M78 985 l6 -3 l5 8 l-4 3 q2 6 8 9 l3 -4 l8 5 l-3 6 q-4 3 -10 0 q-12 -6 -16 -16 q-1 -5 3 -8 z" fill="var(--blue)"/>
      <text class="contact" x="126" y="1006" fill="var(--navy)" transform="translate(2,2)">0911 5372 6140</text>
      <text class="contact" x="126" y="1006">0911 5372 6140</text>
    </g>
    <g class="contact-web">
      <circle cx="404" cy="997" r="25" fill="var(--white)"/>
      <g fill="none" stroke="var(--blue)" stroke-width="2">
        <circle cx="404" cy="997" r="14"/>
        <ellipse cx="404" cy="997" rx="6" ry="14"/>
        <line x1="390" y1="997" x2="418" y2="997"/>
        <line x1="392" y1="990" x2="416" y2="990"/>
        <line x1="392" y1="1004" x2="416" y2="1004"/>
      </g>
      <text class="contact" x="445" y="1006" fill="var(--navy)" transform="translate(2,2)">www.hauskompass24.de</text>
      <text class="contact" x="445" y="1006">www.hauskompass24.de</text>
    </g>
  </svg>

  <h1 class="headline">AUS LIEBE ZU NÜRNBERG<br>ENTSTEHT LEIDENSCHAFT</h1>

  <div class="brand-name">HAUSKOMPASS24</div>
</div>
</body>
</html>
```